I am medical doctor in surgery specialized in Urology and anti-aging. I need Web and Instagram design for a head cream , face cream and body lotion. I did a 2% GHK-Cu solution (head-face-body) with an professional pharmacist specialized in manufacturing creams. . GHK-Cu is a tri-peptide with solid scientific background to rejuvenate the skin (will stimulate collagen production) and can promote hair regrowth. Statistically 70% of peptides bought are fake on the market, I can personally guarantee about purity (my peptides are certified pure above 99% checked in an independent laboratory in London -UK.
I want to use the name 'Lumavex'. I secured already the domain names. I had an design for another project I could re-use for this project. The ribbon should include more blue. The font of Lumavex can be changed. I got a logo which is ok for me. Web design best coded with Wordpress.

Target Market(s)

Anti aging, skin care, hair regrowth, skin collagen

Industry/Entity Type

the cream can also be used after surgery for faster and better wound healing

Number of Pages Required

5+ page

Font styles to use
Sans Serif

Colors
0054AA
0677BA
7BADD7
CADEEF
E8F1F8

Requirements
Must have
• target population 30-70 years
Nice to have
• scientific proof, pictures before-after
Should not have
• GHK-Cu has solid scientific animal studies of anti-cancer properties. It is 100% safe for dermal human use.

```html
<!DOCTYPE html>
<html lang="en">
<head>
<meta charset="utf-8">
<title>Lumavex — Advanced Peptide Science</title>
<link href="https://fonts.googleapis.com/css2?family=Figtree:ital,wght@0,400;0,500;0,600;1,400&family=Libre+Caslon+Text:wght@400;700&display=swap" rel="stylesheet">
<style>
:root{
  --navy:#132f72;
  --navy-deep:#0d2a6b;
  --blue:#0054aa;
  --sky:#7badd7;
  --mist:#cadeef;
  --ice:#e8ebf3;
  --ink:#2b2f3a;
  --muted:#4a4f5c;
  --line:#d6dae3;
  --white:#ffffff;
  --serif:"Libre Caslon Text", Georgia, serif;
  --sans:"Figtree", Arial, sans-serif;
}
*{box-sizing:border-box;margin:0;padding:0}
html,body{width:1200px;height:4243px;overflow:hidden;background:var(--white)}
body{font-family:var(--sans);color:var(--ink);position:relative}
section,header,footer{position:absolute;left:0;width:1200px}
.abs{position:absolute}
.serif{font-family:var(--serif);color:var(--navy);font-weight:700;letter-spacing:-.5px}

/* header */
.site-header{top:0;height:85px;background:var(--white)}
.brand{left:110px;top:20px;font-family:var(--serif);font-weight:700;font-size:36px;color:var(--navy);letter-spacing:-1px}
.main-nav{left:461px;top:31px;display:flex;font-size:16px;color:var(--ink)}
.main-nav span{position:absolute;white-space:nowrap}
.main-nav .active{font-weight:600;color:var(--navy)}
.header-icons{left:995px;top:30px;display:flex;gap:18px}

/* hero */
.hero{top:85px;height:557px;background:linear-gradient(100deg,#2a4d8c 0%,#3f62a0 45%,#7b98c8 100%)}
.hero h1{left:110px;top:122px;font-family:var(--serif);color:var(--white);font-size:45px;line-height:56px;font-weight:700;letter-spacing:-.5px}
.hero h1 .light{font-weight:400;display:block}
.hero p{left:110px;top:266px;width:410px;color:var(--white);font-size:15px;line-height:24px}
.btn-light{left:110px;top:389px;width:163px;height:34px;background:var(--white);color:var(--navy);border-radius:3px;font-size:15px;font-weight:500;display:flex;align-items:center;justify-content:center;gap:4px}
.hero-products{left:675px;top:112px;width:411px;height:409px;border-radius:8px;background:radial-gradient(ellipse at 50% 45%,#f5f7fb 0%,#dfe5ef 45%,rgba(200,170,130,.55) 80%,rgba(120,150,200,0) 100%)}

/* why */
.why{top:642px;height:602px}
.section-title{font-family:var(--serif);font-weight:700;color:var(--navy);letter-spacing:-.5px}
.why .section-title{top:96px;width:100%;text-align:center;font-size:34px}
.why .lead{top:160px;left:200px;width:800px;text-align:center;font-size:15px;line-height:25px;color:var(--ink)}
.feature-card{top:255px;width:231px;height:260px;border:1px solid var(--line);border-radius:4px;background:var(--white);box-shadow:0 2px 6px rgba(20,40,90,.12);text-align:center;padding:24px 20px 0}
.feature-card svg{display:block;margin:0 auto}
.feature-card h3{margin-top:16px;font-size:17px;font-weight:500;color:var(--ink)}
.feature-card p{margin-top:14px;font-size:13px;line-height:19px;color:var(--muted)}

/* peptide */
.peptide{top:1244px;height:843px;background:var(--ice)}
.peptide h2{left:110px;top:78px;font-size:37px;line-height:41px}
.peptide .copy{left:110px;top:184px;width:490px;font-size:15px;line-height:25px;color:var(--ink)}
.peptide .copy p+p{margin-top:10px}
.divider-v{left:633px;top:144px;width:1px;height:163px;background:var(--navy)}
.benefits{left:664px;top:148px;list-style:none;font-size:15px;color:var(--ink)}
.benefits li{display:flex;align-items:center;gap:12px;height:33px}
.molecule{left:930px;top:0;width:270px;height:254px;background:radial-gradient(circle at 60% 40%,rgba(255,255,255,.9) 0%,rgba(200,212,232,.7) 40%,rgba(232,235,243,0) 72%)}
.rule{left:110px;top:395px;width:980px;height:1px;background:var(--navy)}
.peptide h3{top:475px;width:100%;text-align:center;font-size:32px}
.step{top:558px;width:220px;text-align:center}
.step .ring{width:116px;height:116px;border:1.5px solid var(--navy);border-radius:50%;margin:0 auto;display:flex;align-items:center;justify-content:center;background:var(--ice)}
.step h4{margin-top:24px;font-family:var(--serif);font-weight:400;font-size:18px;color:var(--navy)}
.step p{margin-top:6px;font-size:13px;line-height:19px;color:var(--muted)}
.connector{top:616px;height:1.5px;background:var(--navy)}
.chev{top:602px;font-size:26px;color:var(--navy);font-weight:600;background:var(--ice);padding:0 6px;line-height:26px}

/* solutions */
.solutions{top:2087px;height:683px}
.solutions h2{left:110px;top:80px;font-size:35px;line-height:40px}
.product-card{top:206px;width:303px;height:390px;border:1.5px solid #3c5a97;border-radius:3px;background:linear-gradient(180deg,#e3e7ee 0%,#f3f5f8 55%,#e9ecf2 100%);text-align:center}
.product-shot{position:absolute;left:50%;transform:translateX(-50%);border-radius:6px;background:linear-gradient(180deg,#ffffff,#e2e6ee)}
.product-card h3{position:absolute;top:210px;width:100%;font-family:var(--serif);font-weight:400;font-size:20px;color:var(--navy)}
.product-card p{position:absolute;top:250px;left:24px;right:24px;font-size:13px;line-height:19px;color:var(--muted)}
.btn-outline{position:absolute;top:327px;left:70px;width:163px;height:34px;border:1.5px solid var(--navy);border-radius:3px;display:flex;align-items:center;justify-content:center;gap:4px;font-size:14px;font-weight:500;color:var(--navy);background:rgba(255,255,255,.4)}

/* results */
.results{top:2770px;height:632px;background:var(--ice)}
.results h2{top:82px;width:100%;text-align:center;font-size:34px}
.shot{top:175px;height:308px}
.shot .tag{position:absolute;bottom:10px;font-family:var(--serif);font-weight:700;color:var(--white);font-size:13px}
.slider-line{left:253px;top:0;width:3px;height:308px;background:var(--white)}
.slider-handle{left:238px;top:139px;width:32px;height:32px;border-radius:50%;background:rgba(255,255,255,.85);display:flex;align-items:center;justify-content:center}
.dots{top:533px;left:555px;display:flex;gap:9px}
.dots span{width:12px;height:12px;border-radius:50%;border:1.5px solid var(--navy)}
.dots span.on{background:var(--navy)}

/* testimonials */
.testimonials{top:3402px;height:548px}
.testimonials h2{left:110px;top:90px;font-size:34px}
.arrow{top:86px;width:46px;height:46px;border-radius:50%;border:1.5px solid var(--navy);display:flex;align-items:center;justify-content:center}
.arrow.filled{background:var(--navy)}
.review{top:181px;width:313px;height:278px;border:1px solid var(--line);border-radius:4px;background:var(--white);box-shadow:0 2px 6px rgba(20,40,90,.12);padding:36px 26px 0;overflow:hidden}
.review .quote-mark{position:absolute;right:18px;top:-30px;font-family:var(--serif);font-size:200px;color:#eef0f4;line-height:1}
.review blockquote{position:relative;font-style:italic;font-size:13.5px;line-height:21px;color:var(--ink)}
.review .name{position:absolute;left:26px;top:218px;font-family:var(--serif);font-size:18px;color:var(--ink)}
.review .stars{position:absolute;left:26px;top:244px;font-size:10px;color:#e8a21a;letter-spacing:1px}
.review .source{position:absolute;right:26px;top:218px;width:36px;height:36px;border-radius:50%;border:5px solid #4a78c8}

/* footer */
.site-footer{top:3950px;height:293px;background:var(--navy-deep)}
.footer-brand{top:48px;width:100%;text-align:center;font-family:var(--serif);font-weight:700;font-size:48px;color:var(--white);letter-spacing:-1px}
.footer-nav{top:168px;left:0;width:100%;display:flex;justify-content:center;gap:52px;font-size:18px;color:var(--white)}
.footer-rule{left:110px;top:224px;width:980px;height:1px;background:rgba(255,255,255,.55)}
.copyright{top:249px;width:100%;text-align:center;font-size:13px;color:var(--white)}
</style>
</head>
<body>

<header class="site-header">
  <div class="abs brand">Lumavex</div>
  <nav class="abs main-nav">
    <span class="active" style="left:0">Home</span>
    <span style="left:84px">Products</span>
    <span style="left:184px">Science</span>
    <span style="left:276px">About</span>
    <span style="left:359px">FAQ</span>
    <span style="left:426px">Contact</span>
  </nav>
  <div class="abs header-icons">
    <svg width="20" height="20" viewBox="0 0 20 20" fill="none" stroke="#222" stroke-width="1.8"><circle cx="8.5" cy="8.5" r="6"/><path d="M13 13l5 5"/></svg>
    <svg width="20" height="20" viewBox="0 0 20 20" fill="none" stroke="#222" stroke-width="1.8"><circle cx="10" cy="6.5" r="4"/><path d="M2.5 19c0-4.5 3.5-7 7.5-7s7.5 2.5 7.5 7"/></svg>
    <svg width="20" height="20" viewBox="0 0 20 20" fill="none" stroke="#222" stroke-width="1.8"><rect x="3" y="5" width="14" height="13" rx="2"/><path d="M7 8V5a3 3 0 016 0v3"/></svg>
  </div>
</header>

<section class="hero" role="img" aria-label="Soft blue backdrop with faint molecule structures">
  <h1 class="abs">Advanced Peptide Science<span class="light">For Healthier Skin Hair</span></h1>
  <p class="abs">Powered by 99%+ certified pure GHK-Cu peptide, Lumavex combines medical expertise with pharmaceutical precision to support healthier-looking skin, improved elasticity, &amp; fuller-looking hair.</p>
  <div class="abs btn-light">Shop Collection <span>&raquo;</span></div>
  <div class="abs hero-products" role="img" aria-label="Face cream tube, body lotion pump bottle and head cream jar on a wooden slab"></div>
</section>

<section class="why">
  <h2 class="abs section-title">Why Choose Lumavex?</h2>
  <p class="abs lead">Not all peptides are created equal. Lumavex was developed to deliver exceptional purity, scientific integrity, and professional skincare backed by medical expertise</p>

  <div class="abs feature-card" style="left:110px">
    <svg width="66" height="66" viewBox="0 0 66 66" fill="none" stroke="#132f72" stroke-width="2"><path d="M14 26l9-11h20l9 11L33 52z"/><path d="M14 26h38M23 15l10 37 10-37M33 15v0"/><path d="M33 4v5M18 8l3 4M48 8l-3 4"/></svg>
    <h3>99%+ Certified Pure</h3>
    <p>Every batch is independently verified for exceptional purity. ensuring you receive authentic GHK-Cu peptide of the highest quality</p>
  </div>
  <div class="abs feature-card" style="left:359px">
    <svg width="66" height="66" viewBox="0 0 66 66" fill="none" stroke="#132f72" stroke-width="2"><circle cx="33" cy="33" r="24"/><path d="M33 20v26M20 33h26"/></svg>
    <h3>Doctor Developed</h3>
    <p>Created by a surgeon specializing in anti-aging medicine, comtiming clinical knowledge with advanced peptide science.</p>
  </div>
  <div class="abs feature-card" style="left:608px">
    <svg width="66" height="66" viewBox="0 0 66 66" fill="none" stroke="#132f72" stroke-width="2"><path d="M22 8h12M25 8v18M31 8v18"/><circle cx="28" cy="38" r="12"/><path d="M12 58h34M20 50v8M36 50v8"/><path d="M46 36h8M48 36v8l-5 14h14l-5-14v-8"/><circle cx="52" cy="18" r="2.5"/><circle cx="57" cy="26" r="2"/></svg>
    <h3>Pharmaceutical Precision</h3>
    <p>Manufactured in collaboration with an experienced pharmaceutical compounding specialist using rigorous quality standards</p>
  </div>
  <div class="abs feature-card" style="left:857px">
    <svg width="66" height="66" viewBox="0 0 66 66" fill="none" stroke="#132f72" stroke-width="2"><ellipse cx="33" cy="33" rx="26" ry="10"/><ellipse cx="33" cy="33" rx="26" ry="10" transform="rotate(60 33 33)"/><ellipse cx="33" cy="33" rx="26" ry="10" transform="rotate(-60 33 33)"/><circle cx="33" cy="33" r="4"/></svg>
    <h3>Trusted Science</h3>
    <p>GHK-Cu is one of the most extensively researched peptides for supporting healthier-looking skin and scalp.</p>
  </div>
</section>

<section class="peptide">
  <div class="abs molecule" role="img" aria-label="Glassy molecule structure decoration"></div>
  <h2 class="abs serif">The Peptide Behind<br>The Transformation</h2>
  <div class="abs copy">
    <p>GHK-Cu is a naturally occurring copper peptide recognized for its ability to support the skin's natural renewal process.</p>
    <p>As we age, natural levels decline. Lumavex replenishes this important peptide through carefully formulated topical applications designed for daily use</p>
  </div>
  <div class="abs divider-v"></div>
  <ul class="abs benefits">
    <li><svg width="15" height="15" viewBox="0 0 15 15"><circle cx="7.5" cy="7.5" r="7.5" fill="#132f72"/><path d="M6 4.5l3 3-3 3" stroke="#fff" stroke-width="1.6" fill="none"/></svg>Supports collagen production</li>
    <li><svg width="15" height="15" viewBox="0 0 15 15"><circle cx="7.5" cy="7.5" r="7.5" fill="#132f72"/><path d="M6 4.5l3 3-3 3" stroke="#fff" stroke-width="1.6" fill="none"/></svg>Improves the appearance of fine lines</li>
    <li><svg width="15" height="15" viewBox="0 0 15 15"><circle cx="7.5" cy="7.5" r="7.5" fill="#132f72"/><path d="M6 4.5l3 3-3 3" stroke="#fff" stroke-width="1.6" fill="none"/></svg>Promotes firmer-looking skin</li>
    <li><svg width="15" height="15" viewBox="0 0 15 15"><circle cx="7.5" cy="7.5" r="7.5" fill="#132f72"/><path d="M6 4.5l3 3-3 3" stroke="#fff" stroke-width="1.6" fill="none"/></svg>Helps maintain skin hydration</li>
    <li><svg width="15" height="15" viewBox="0 0 15 15"><circle cx="7.5" cy="7.5" r="7.5" fill="#132f72"/><path d="M6 4.5l3 3-3 3" stroke="#fff" stroke-width="1.6" fill="none"/></svg>Supports healthier-looking hair</li>
  </ul>
  <div class="abs rule"></div>

  <h3 class="abs serif">Inspired by Nature. Backed by Science.</h3>

  <div class="abs connector" style="left:265px;width:146px"></div>
  <div class="abs connector" style="left:527px;width:146px"></div>
  <div class="abs connector" style="left:789px;width:146px"></div>
  <div class="abs chev" style="left:322px">&raquo;</div>
  <div class="abs chev" style="left:584px">&raquo;</div>
  <div class="abs chev" style="left:846px">&raquo;</div>

  <div class="abs step" style="left:97px">
    <div class="ring"><svg width="62" height="50" viewBox="0 0 62 50" fill="none" stroke="#132f72" stroke-width="1.8"><path d="M18 6l22 20M26 4l18 16"/><path d="M4 32c8-4 14 4 22 0s14 4 22 0 10 2 10 2"/><path d="M6 42h2M16 44h2M26 42h2M36 44h2M46 42h2"/></svg></div>
    <h4>01 - Apply</h4><p>Massage Lumavex gently onto clean skin or scalp.</p>
  </div>
  <div class="abs step" style="left:359px">
    <div class="ring"><svg width="56" height="56" viewBox="0 0 56 56" fill="none" stroke="#132f72" stroke-width="1.8"><path d="M8 14l14-8 18 8v14c0 12-10 20-18 22C14 48 8 40 8 28z"/><circle cx="34" cy="34" r="9"/><path d="M41 41l9 9"/></svg></div>
    <h4>02 - Penetrate</h4><p>Our formulation helps deliver GHK-Cu</p>
  </div>
  <div class="abs step" style="left:621px">
    <div class="ring"><svg width="62" height="56" viewBox="0 0 62 56" fill="none" stroke="#132f72" stroke-width="1.8"><path d="M31 4c-5 8-9 12-9 17a9 9 0 0018 0c0-5-4-9-9-17z"/><path d="M4 34h54"/><circle cx="12" cy="44" r="2"/><circle cx="24" cy="46" r="2"/><circle cx="36" cy="44" r="2"/><circle cx="48" cy="46" r="2"/></svg></div>
    <h4>03 - Signal</h4><p>GHK-Cu communicates with skin cells, supporting</p>
  </div>
  <div class="abs step" style="left:883px">
    <div class="ring"><svg width="56" height="56" viewBox="0 0 56 56" fill="none" stroke="#132f72" stroke-width="1.8"><path d="M28 8l3 9 9 3-9 3-3 9-3-9-9-3 9-3z"/><path d="M44 34l2 5 5 2-5 2-2 5-2-5-5-2 5-2z"/><path d="M12 36l1.5 4 4 1.5-4 1.5-1.5 4-1.5-4-4-1.5 4-1.5z"/></svg></div>
    <h4>04 - Renew</h4><p>Regular use helps support smoother, healthier-looking</p>
  </div>
</section>

<section class="solutions">
  <h2 class="abs serif">One Science. Three Specialized<br>Solutions.</h2>

  <div class="abs product-card" style="left:110px">
    <div class="product-shot" role="img" aria-label="Head cream jar" style="top:76px;width:118px;height:84px;border-radius:14px"></div>
    <h3>Head Cream</h3>
    <p>Supports healthier-looking hair and scalp while helping maintain a fulier appearance.</p>
    <div class="btn-outline">Learn More <span>&raquo;</span></div>
  </div>
  <div class="abs product-card" style="left:449px">
    <div class="product-shot" role="img" aria-label="Face cream tube" style="top:26px;width:58px;height:164px;border-radius:6px 6px 16px 16px"></div>
    <h3>Face Cream</h3>
    <p>Designed to improve skin texture, elasticity, and hydration for a refreshed appearance</p>
    <div class="btn-outline">Learn More <span>&raquo;</span></div>
  </div>
  <div class="abs product-card" style="left:787px">
    <div class="product-shot" role="img" aria-label="Body lotion pump bottle" style="top:30px;width:54px;height:160px;border-radius:12px 12px 6px 6px"></div>
    <h3>Body Lotion</h3>
    <p>Nourishes larger areas of the body while supporting smoother, healthier-looking skin.</p>
    <div class="btn-outline">Learn More <span>&raquo;</span></div>
  </div>
</section>

<section class="results">
  <h2 class="abs section-title">Visible Improvements Over Time</h2>

  <div class="abs shot" role="img" aria-label="After photo of a smooth neck and jawline" style="left:104px;width:194px;background:linear-gradient(90deg,#f4f1ee,#c9b6a8 60%,#d9c8bb)">
    <span class="tag" style="right:10px">After</span>
  </div>
  <div class="abs shot" role="img" aria-label="Before and after comparison of cheek skin texture" style="left:346px;width:508px;background:linear-gradient(90deg,#c98b78 0%,#d79c88 48%,#dfb19e 52%,#e6bfae 100%)">
    <span class="tag" style="left:16px">Before</span>
    <span class="tag" style="right:10px">After</span>
    <div class="abs slider-line"></div>
    <div class="abs slider-handle"><svg width="16" height="12" viewBox="0 0 16 12" fill="none" stroke="#333" stroke-width="1.6"><path d="M5 2L1 6l4 4M11 2l4 4-4 4"/></svg></div>
  </div>
  <div class="abs shot" role="img" aria-label="Before photo of a cheek with a hand touching skin" style="left:902px;width:193px;background:linear-gradient(90deg,#d9b7a6,#e9d3c6 60%,#efe4dc)">
    <span class="tag" style="left:38px">Before</span>
  </div>

  <div class="abs dots"><span class="on"></span><span></span><span></span><span></span></div>
</section>

<section class="testimonials">
  <h2 class="abs section-title">Our Testimonials</h2>
  <div class="abs arrow filled" style="left:971px"><svg width="14" height="20" viewBox="0 0 14 20" fill="none" stroke="#fff" stroke-width="2.4"><path d="M11 2L3 10l8 8"/></svg></div>
  <div class="abs arrow" style="left:1040px"><svg width="14" height="20" viewBox="0 0 14 20" fill="none" stroke="#132f72" stroke-width="2"><path d="M3 2l8 8-8 8"/></svg></div>

  <article class="abs review" style="left:110px">
    <span class="quote-mark">&ldquo;</span>
    <blockquote>"Lorem ipsum dolor sit amet, consec tetur adipiscing elit, sed do eiusmod tempor incid idunt ut labore et do lore magna aliqua. Quis ipsum susp end isse ultrices gravida. Risus com modo viverra mae cenas accu msan lacus vel facilisis. "</blockquote>
    <div class="name">Daniel Hart</div><div class="stars">★★★★★</div><div class="source"></div>
  </article>
  <article class="abs review" style="left:444px">
    <span class="quote-mark">&ldquo;</span>
    <blockquote>"Lorem ipsum dolor sit amet, consec tetur adipiscing elit, sed do eiusmod tempor incid idunt ut labore et do lore magna aliqua. Quis ipsum susp end isse ultrices gravida. Risus com modo viverra mae cenas accu msan lacus vel facilisis. "</blockquote>
    <div class="name">Daniel Hart</div><div class="stars">★★★★★</div><div class="source"></div>
  </article>
  <article class="abs review" style="left:777px">
    <span class="quote-mark">&ldquo;</span>
    <blockquote>"Lorem ipsum dolor sit amet, consec tetur adipiscing elit, sed do eiusmod tempor incid idunt ut labore et do lore magna aliqua. Quis ipsum susp end isse ultrices gravida. Risus com modo viverra mae cenas accu msan lacus vel facilisis. "</blockquote>
    <div class="name">Daniel Hart</div><div class="stars">★★★★★</div><div class="source"></div>
  </article>
</section>

<footer class="site-footer">
  <div class="abs footer-brand">Lumavex</div>
  <nav class="abs footer-nav"><span>Home</span><span>Products</span><span>Science</span><span>About</span><span>FAQ</span><span>Contact</span></nav>
  <div class="abs footer-rule"></div>
  <div class="abs copyright">© 2026 Lumavex. All rights reserved.</div>
</footer>

</body>
</html>
```